Sign listing benefits of Wash and Fold Service

Sign 48 inches wide and 24 inches height to showcase service listed above.
Benefits include:
Saves Money
Saves Time
Convenient
Stain Treatment

Looking for something colorful (Blue and white are our business colors) the look of a laundromat business.

```html
<!DOCTYPE html>
<html lang="en">
<head>
<meta charset="utf-8">
<title>Wash and Dry Fold Benefits Sign</title>
<link href="https://fonts.googleapis.com/css2?family=Montserrat:wght@700;800;900&display=swap" rel="stylesheet">
<style>
  :root {
    --page: #c9c9c9;
    --sky-light: #b9ecfb;
    --sky-mid: #4cc0e8;
    --sky-deep: #1aa0d8;
    --royal: #0b47c0;
    --royal-bright: #2f8ee8;
    --silver-light: #ffffff;
    --silver-mid: #dfe4ec;
    --silver-dark: #9aa3b0;
    --ink-shadow: rgba(10, 30, 80, 0.55);
    --tick: #0c4fd0;
    --photo-warm: #d99a66;
    --photo-cool: #a9d6ee;
  }
  * { margin: 0; padding: 0; box-sizing: border-box; }
  html, body { width: 1200px; height: 1200px; overflow: hidden; }
  body {
    background: var(--page);
    font-family: "Montserrat", Arial, sans-serif;
    position: relative;
  }
  .sign {
    position: absolute;
    left: 80px;
    top: 340px;
    width: 1040px;
    height: 520px;
    overflow: hidden;
    background: radial-gradient(circle at 530px 250px, var(--sky-light) 0%, var(--sky-mid) 40%, var(--sky-deep) 80%);
    box-shadow: 0 22px 26px -14px rgba(0,0,0,0.35);
  }
  .bubbles, .wave { position: absolute; inset: 0; width: 1040px; height: 520px; }
  .service-photo {
    position: absolute;
    left: 560px;
    top: 18px;
    width: 415px;
    height: 450px;
    border-radius: 180px 180px 10px 10px;
    background: linear-gradient(160deg, var(--photo-cool) 0%, #c9a58a 45%, var(--photo-warm) 100%);
    opacity: 0.85;
  }
  .silver-text {
    background: linear-gradient(180deg, var(--silver-light) 0%, var(--silver-mid) 55%, var(--silver-dark) 100%);
    -webkit-background-clip: text;
    background-clip: text;
    color: transparent;
    filter: drop-shadow(2px 3px 2px var(--ink-shadow));
    font-weight: 900;
    white-space: nowrap;
    position: absolute;
  }
  .headline-lead { left: 128px; top: 56px; font-size: 40px; letter-spacing: 1px; }
  .headline-band {
    position: absolute;
    left: 0;
    top: 106px;
    width: 617px;
    height: 54px;
    border-radius: 0 27px 27px 0;
    background: linear-gradient(90deg, var(--royal) 0%, var(--royal-bright) 100%);
  }
  .headline-main { left: 47px; top: 105px; font-size: 45px; letter-spacing: 0.5px; }
  .benefits { position: absolute; left: 39px; top: 179px; list-style: none; }
  .benefit { display: flex; align-items: center; height: 51.5px; }
  .benefit svg { width: 40px; height: 40px; flex: none; }
  .benefit-label { position: static; margin-left: 19px; font-size: 33px; font-weight: 800; }
  .call-label { left: 98px; top: 419px; font-size: 23px; font-weight: 800; }
  .call-row { position: absolute; left: 42px; top: 458px; display: flex; align-items: center; }
  .call-row svg { width: 42px; height: 42px; flex: none; }
  .phone-number { position: static; margin-left: 10px; font-size: 47px; letter-spacing: 0.5px; }
</style>
</head>
<body>
  <section class="sign">
    <div class="service-photo" role="img" aria-label="Photo of a smiling woman holding a stack of freshly folded knit sweaters"></div>

    <svg class="bubbles" viewBox="0 0 1040 520" aria-hidden="true">
      <defs>
        <radialGradient id="bubble-fill" cx="50%" cy="50%" r="50%">
          <stop offset="70%" stop-color="#ffffff" stop-opacity="0.05"/>
          <stop offset="100%" stop-color="#ffffff" stop-opacity="0.55"/>
        </radialGradient>
      </defs>
      <g fill="url(#bubble-fill)" stroke="#ffffff" stroke-opacity="0.6" stroke-width="1.5">
        <circle cx="28" cy="30" r="34"/>
        <circle cx="1037" cy="27" r="34"/>
        <circle cx="645" cy="64" r="42"/>
        <circle cx="1058" cy="268" r="40"/>
        <circle cx="537" cy="391" r="42"/>
        <circle cx="654" cy="409" r="24"/>
      </g>
    </svg>

    <svg class="wave" viewBox="0 0 1040 520" aria-hidden="true">
      <defs>
        <linearGradient id="wave-silver" x1="0" x2="1">
          <stop offset="0" stop-color="#a7adb6"/>
          <stop offset="0.45" stop-color="#f4f6f8"/>
          <stop offset="1" stop-color="#7f868e"/>
        </linearGradient>
        <linearGradient id="wave-blue" x1="0" x2="1" y1="0" y2="0.3">
          <stop offset="0" stop-color="#0a3fb8"/>
          <stop offset="0.6" stop-color="#2a8ee9"/>
          <stop offset="1" stop-color="#1f7fe0"/>
        </linearGradient>
      </defs>
      <path d="M0,418 C200,366 430,405 640,440 C840,474 990,450 1040,388 L1040,520 L0,520 Z" fill="url(#wave-silver)"/>
      <path d="M0,432 C200,385 440,425 650,457 C850,487 990,476 1040,424 L1040,520 L0,520 Z" fill="url(#wave-blue)"/>
    </svg>

    <div class="silver-text headline-lead">BENEFITS OF</div>
    <div class="headline-band"></div>
    <div class="silver-text headline-main">WASH AND DRY FOLD</div>

    <ul class="benefits">
      <li class="benefit">
        <svg viewBox="0 0 40 40" aria-hidden="true"><path d="M33,12 A17,17 0 1 0 36,20" fill="none" stroke="var(--tick)" stroke-width="3"/><path d="M11,19 L18,26 L34,9" fill="none" stroke="var(--tick)" stroke-width="4" stroke-linecap="round" stroke-linejoin="round"/></svg>
        <span class="silver-text benefit-label">SAVES MONEY</span>
      </li>
      <li class="benefit">
        <svg viewBox="0 0 40 40" aria-hidden="true"><path d="M33,12 A17,17 0 1 0 36,20" fill="none" stroke="var(--tick)" stroke-width="3"/><path d="M11,19 L18,26 L34,9" fill="none" stroke="var(--tick)" stroke-width="4" stroke-linecap="round" stroke-linejoin="round"/></svg>
        <span class="silver-text benefit-label">SAVES TIME</span>
      </li>
      <li class="benefit">
        <svg viewBox="0 0 40 40" aria-hidden="true"><path d="M33,12 A17,17 0 1 0 36,20" fill="none" stroke="var(--tick)" stroke-width="3"/><path d="M11,19 L18,26 L34,9" fill="none" stroke="var(--tick)" stroke-width="4" stroke-linecap="round" stroke-linejoin="round"/></svg>
        <span class="silver-text benefit-label">CONVENIENT</span>
      </li>
      <li class="benefit">
        <svg viewBox="0 0 40 40" aria-hidden="true"><path d="M33,12 A17,17 0 1 0 36,20" fill="none" stroke="var(--tick)" stroke-width="3"/><path d="M11,19 L18,26 L34,9" fill="none" stroke="var(--tick)" stroke-width="4" stroke-linecap="round" stroke-linejoin="round"/></svg>
        <span class="silver-text benefit-label">STAIN TREATMENT</span>
      </li>
    </ul>

    <div class="silver-text call-label">CALL US:</div>
    <div class="call-row">
      <svg viewBox="0 0 42 42" aria-hidden="true">
        <circle cx="21" cy="21" r="19" fill="#f2f4f8" stroke="#aab2bf" stroke-width="2"/>
        <path d="M14,11 C12,12 11,14 12,17 C14,23 19,28 25,30 C28,31 30,30 31,28 L28,24 C27,23 26,23 25,24 L23,25 C20,23 19,22 17,19 L18,17 C19,16 19,15 18,14 Z" fill="#0b47c0"/>
      </svg>
      <span class="silver-text phone-number">000.000.000</span>
    </div>
  </section>
</body>
</html>
```